" Somos uma escola de Yoga e oferecemos aulas, Cursos de Formaçao para Professores de Yoga, workshops e retiros de meditaçao pelo Brasil e em países como Costa Rica, Panamá, Bali e Tailandia. Trabalhamos com o metodo Yin e Yang.. onde yin é a energia da meditaçao, contemplaçao e observaçao e yang do movimento, rítmo, força e atividade. "

```html
<!DOCTYPE html>
<html lang="pt-BR">
<head>
<meta charset="UTF-8">
<title>Prana Viva Yoga School – Marcadores</title>
<link rel="stylesheet" href="https://fonts.googleapis.com/css2?family=Open+Sans:wght@400;600;700&display=swap">
<style>
  :root {
    --green: #6bb52f;
    --green-dark: #4e9321;
    --green-light: #a6d46f;
    --green-pale: #d9edc2;
    --white: #ffffff;
    --ink: #222222;
    --page: #ececec;
  }
  * { box-sizing: border-box; margin: 0; padding: 0; }
  html, body { width: 1200px; height: 1200px; overflow: hidden; }
  body {
    background: var(--page);
    font-family: "Open Sans", sans-serif;
    position: relative;
  }
  .bookmark {
    position: absolute;
    top: 100px;
    width: 290px;
    height: 1000px;
    background: var(--white);
    box-shadow: 0 6px 18px rgba(0,0,0,.18);
    overflow: hidden;
  }
  .bookmark--front { left: 250px; }
  .bookmark--back { left: 660px; background: var(--green); }

  /* front */
  .band { position: absolute; left: 0; width: 100%; background: var(--green); }
  .band--top { top: 40px; height: 30px; }
  .band--bottom { top: 930px; height: 30px; }
  .ornament {
    position: absolute; left: 0; top: 170px;
    width: 290px; height: 460px;
    background:
      radial-gradient(circle at 50% 50%, var(--white) 0 38%, var(--green-pale) 46%, var(--green-light) 58%, var(--green) 68%, var(--green-light) 76%, var(--white) 88%);
  }
  .ornament__name {
    position: absolute; inset: 0;
    display: flex; align-items: center; justify-content: center;
    font-size: 28px; font-weight: 700; color: var(--ink);
  }
  .brand {
    position: absolute; left: 0; width: 100%;
    text-align: center; color: var(--ink);
  }
  .brand--front { top: 700px; }
  .brand__dot {
    display: block; margin: 0 auto 10px;
    width: 46px; height: 46px; border-radius: 50%;
    background: var(--green);
  }
  .brand__name { font-size: 24px; font-weight: 600; line-height: 1.2; }
  .brand__tag { font-size: 11px; letter-spacing: 3px; margin-top: 2px; }

  /* back */
  .back__head {
    position: absolute; top: 0; left: 0; width: 100%; height: 165px;
    background: var(--white);
  }
  .brand--back { top: 38px; }
  .brand--back .brand__dot { width: 40px; height: 40px; }
  .brand--back .brand__name { font-size: 20px; }
  .about {
    position: absolute; top: 300px; left: 50px; right: 50px;
    color: var(--white); font-size: 13px; font-weight: 600;
    line-height: 1.35; text-align: center;
  }
  .seal {
    position: absolute; top: 640px; left: 115px;
    width: 60px; height: 60px; border-radius: 50%;
    border: 3px solid var(--white);
  }
  .contacts {
    position: absolute; top: 730px; left: 40px; right: 16px;
    list-style: none; color: var(--white);
    font-size: 12.5px; font-weight: 600;
  }
  .contacts li { display: flex; align-items: center; gap: 8px; height: 24px; white-space: nowrap; }
  .contacts svg { width: 16px; height: 16px; flex: none; }
  .back__foot {
    position: absolute; top: 905px; left: 0; width: 100%; height: 95px;
    border-top: 4px solid var(--white);
    background: var(--green);
    color: var(--white); font-size: 12px; font-weight: 600;
    display: flex; align-items: center; justify-content: center;
  }
</style>
</head>
<body>

<section class="bookmark bookmark--front">
  <div class="band band--top"></div>
  <div class="ornament" role="img" aria-label="Mandala ornamental verde com coroa de folhas em volta do símbolo da escola">
    <span class="ornament__name">Prana Viva</span>
  </div>
  <div class="brand brand--front">
    <span class="brand__dot"></span>
    <p class="brand__name">prana viva</p>
    <p class="brand__tag">YOGA SCHOOL</p>
  </div>
  <div class="band band--bottom"></div>
</section>

<section class="bookmark bookmark--back">
  <header class="back__head">
    <div class="brand brand--back">
      <span class="brand__dot"></span>
      <p class="brand__name">prana viva</p>
      <p class="brand__tag">YOGA SCHOOL</p>
    </div>
  </header>

  <p class="about">Informações sobre a empresa, Informações sobre a empresa, Informações sobre a empresa, Informações sobre a empresa, Informações sobre a empresa, Informações sobre a empresa, Informações sobre a empresa, Informações sobre a empresa, Informações sobre a empresa, Informações sobre a empresa, Informações sobre a empresa.</p>

  <span class="seal"></span>

  <ul class="contacts">
    <li><svg viewBox="0 0 16 16"><circle cx="8" cy="8" r="8" fill="#fff"/><path d="M5 4.5l1.6-.4.8 2-1 .8a6 6 0 0 0 2.7 2.7l.8-1 2 .8-.4 1.6c-3.5.3-6.8-3-6.5-6.5z" fill="#6bb52f"/></svg>+55 11 4000-1234</li>
    <li><svg viewBox="0 0 16 16"><circle cx="8" cy="8" r="8" fill="#fff"/><rect x="5.5" y="3.5" width="5" height="9" rx="1" fill="#6bb52f"/><rect x="6.3" y="4.6" width="3.4" height="5.8" fill="#fff"/><circle cx="8" cy="11.5" r=".5" fill="#fff"/></svg>+55 11 4000-5678</li>
    <li><svg viewBox="0 0 16 16"><circle cx="8" cy="8" r="8" fill="#fff"/><circle cx="8" cy="8" r="1.8" fill="none" stroke="#6bb52f" stroke-width="1.3"/><path d="M9.8 6.5v2.3c0 1 1.6 1 1.6-.6A3.5 3.5 0 1 0 10 11" fill="none" stroke="#6bb52f" stroke-width="1.3" stroke-linecap="round"/></svg>@pranavivayoga</li>
    <li><svg viewBox="0 0 16 16"><circle cx="8" cy="8" r="8" fill="#fff"/><path d="M7 9l2-2M6.2 7.6 5 8.8a1.6 1.6 0 0 0 2.2 2.2l1.2-1.2M9.8 8.4 11 7.2A1.6 1.6 0 0 0 8.8 5L7.6 6.2" fill="none" stroke="#6bb52f" stroke-width="1.3" stroke-linecap="round"/></svg>/pranavivayoga</li>
    <li><svg viewBox="0 0 16 16"><circle cx="8" cy="8" r="8" fill="#fff"/><circle cx="8" cy="8" r="5" fill="none" stroke="#6bb52f" stroke-width="1.2"/><path d="M3 8h10M8 3c-2 2.5-2 7.5 0 10M8 3c2 2.5 2 7.5 0 10" fill="none" stroke="#6bb52f" stroke-width="1"/></svg>pranavivayoga.com.br</li>
    <li><svg viewBox="0 0 16 16"><circle cx="8" cy="8" r="8" fill="#fff"/><path d="M8 3.5a3 3 0 0 0-3 3c0 2.2 3 6 3 6s3-3.8 3-6a3 3 0 0 0-3-3z" fill="#6bb52f"/><circle cx="8" cy="6.5" r="1" fill="#fff"/></svg>Rua das Flores, 100, SP</li>
  </ul>

  <footer class="back__foot">www.pranaviva.com.br</footer>
</section>

</body>
</html>
```